Stationary & Business cards for Onsite Wastewater Company
Brindlecove Septic Systems Ltd.
Stationary & Business cards for Onsite Wastewater Company - Construction
Creative Brief
Professional
Dwight Amberole
6172 Pellworth St. Harrowmere, H.C. V3K8R2
dwight@brindlecoveseptic-example.com
brindlecoveseptic-example.com
I would like it to say: Design & Build on the front of the card
Open to ideas: maybe use the logo with black background
lanternmoth lanternmoth

```html
<!DOCTYPE html>
<html lang="en">
<head>
<meta charset="utf-8">
<title>Brindlecove Septic Systems Ltd. — Business Cards</title>
<link rel="stylesheet" href="https://fonts.googleapis.com/css2?family=Open+Sans:wght@400;600&family=Titillium+Web:wght@700&display=swap">
<style>
  :root {
    --page-bg: #e9e9ea;
    --card-black: #0b0b0c;
    --brand-blue: #1d86c9;
    --brand-blue-light: #3fb0ea;
    --silver: #cfd2d6;
    --text-light: #e6e8ea;
    --text-dark: #2a2c2f;
  }
  * { margin: 0; padding: 0; box-sizing: border-box; }
  html, body {
    width: 1200px; height: 901px; overflow: hidden;
    background: radial-gradient(ellipse at 50% 40%, #f7f7f8 0%, var(--page-bg) 75%);
    font-family: "Open Sans", Arial, sans-serif;
  }
  .card {
    position: absolute; left: 280px; width: 640px; height: 366px;
    background: var(--card-black); overflow: hidden;
    box-shadow: 0 14px 30px rgba(0,0,0,0.28);
  }
  .card--front { top: 60px; }
  .card--back { top: 475px; }
  .card-bands { position: absolute; inset: 0; width: 640px; height: 366px; }
  .brand-name {
    font-family: "Titillium Web", Arial, sans-serif; font-weight: 700;
    color: var(--silver); text-transform: uppercase; letter-spacing: 1px;
    line-height: 1.02;
  }
  .card--front .brand-name {
    position: absolute; left: 150px; top: 100px; width: 340px;
    font-size: 44px; text-align: center;
  }
  .brand-name .brand-sub { display: block; font-size: 0.5em; letter-spacing: 2px; }
  .website {
    position: absolute; left: 34px; top: 318px;
    font-size: 17px; color: var(--text-dark); letter-spacing: 0.3px;
  }
  .contact { position: absolute; left: 56px; top: 48px; color: var(--text-light); }
  .contact-name { font-size: 20px; font-weight: 400; margin-bottom: 14px; }
  .contact-list { list-style: none; font-size: 13px; line-height: 19px; }
  .contact-list li { display: flex; align-items: flex-start; gap: 8px; white-space: nowrap; }
  .contact-icon { width: 12px; height: 12px; margin-top: 4px; flex: none; fill: var(--brand-blue-light); }
  .contact-list .no-icon { padding-left: 20px; }
  .divider {
    position: absolute; left: 362px; top: 60px; width: 2px; height: 200px;
    background: linear-gradient(to bottom, transparent, #cfd2d6 50%, transparent);
  }
  .card--back .brand-name {
    position: absolute; left: 382px; top: 118px; width: 240px;
    font-size: 34px; text-align: center;
  }
  .tagline {
    position: absolute; left: 48px; top: 300px;
    font-size: 17px; color: var(--text-dark);
  }
</style>
</head>
<body>

<section class="card card--front" aria-label="Business card front">
  <svg class="card-bands" viewBox="0 0 640 366" aria-hidden="true">
    <defs>
      <linearGradient id="frontBlue" x1="0" y1="0" x2="1" y2="0">
        <stop offset="0" stop-color="#145f92"/>
        <stop offset="1" stop-color="#3fb0ea"/>
      </linearGradient>
      <linearGradient id="frontStrip" x1="0" y1="0" x2="1" y2="0">
        <stop offset="0" stop-color="#ffffff"/>
        <stop offset="1" stop-color="#b8bcc1"/>
      </linearGradient>
    </defs>
    <polygon points="0,268 640,212 640,366 0,366" fill="url(#frontBlue)"/>
    <polygon points="0,298 640,244 640,366 0,366" fill="url(#frontStrip)"/>
  </svg>
  <div class="brand-name">Brindlecove<span class="brand-sub">Septic Systems Ltd.</span></div>
  <p class="website">brindlecoveseptic-example.com</p>
</section>

<section class="card card--back" aria-label="Business card back">
  <svg class="card-bands" viewBox="0 0 640 366" aria-hidden="true">
    <defs>
      <linearGradient id="backBlue" x1="0" y1="0" x2="1" y2="0">
        <stop offset="0" stop-color="#145f92"/>
        <stop offset="1" stop-color="#3fb0ea"/>
      </linearGradient>
      <linearGradient id="backGrey" x1="0" y1="0" x2="1" y2="0">
        <stop offset="0" stop-color="#f4f5f6"/>
        <stop offset="1" stop-color="#9ea3a8"/>
      </linearGradient>
    </defs>
    <polygon points="322,276 640,238 640,366 390,366" fill="url(#backBlue)"/>
    <polygon points="0,284 328,284 390,366 0,366" fill="url(#backGrey)"/>
  </svg>

  <div class="contact">
    <p class="contact-name">Dwight Amberole</p>
    <ul class="contact-list">
      <li><svg class="contact-icon" viewBox="0 0 12 12"><path d="M6 0a4 4 0 0 0-4 4c0 3 4 8 4 8s4-5 4-8a4 4 0 0 0-4-4zm0 5.6A1.6 1.6 0 1 1 6 2.4a1.6 1.6 0 0 1 0 3.2z"/></svg><span>6172 Pellworth St.</span></li>
      <li class="no-icon">Harrowmere, H.C.</li>
      <li class="no-icon">V3K8R2</li>
      <li><svg class="contact-icon" viewBox="0 0 12 12"><path d="M2.4 0.5l2 2.6-1.2 1.4a7 7 0 0 0 4.3 4.3l1.4-1.2 2.6 2-1.1 1.9C5 11.2 0.8 7 .5 1.6z"/></svg><span>604-555-0142</span></li>
      <li><svg class="contact-icon" viewBox="0 0 12 12"><rect x="3" y="0.5" width="6" height="11" rx="1.2"/></svg><span>604-555-0187</span></li>
      <li><svg class="contact-icon" viewBox="0 0 12 12"><path d="M0 2h12v8H0zM0.6 2.4L6 6.6l5.4-4.2" stroke="#0b0b0c" stroke-width="0.9"/></svg><span>dwight@brindlecoveseptic-example.com</span></li>
    </ul>
  </div>

  <div class="divider" aria-hidden="true"></div>
  <div class="brand-name">Brindlecove<span class="brand-sub">Septic Systems Ltd.</span></div>
  <p class="tagline">Design &amp; Build</p>
</section>

</body>
</html>
```